The Hollow - Short Film Poster Design

A short film that follows a forest ranger contemplating suicide as he stumbles upon three kids lost in the forest, each in their own, different way.

Genre: Contemporary Dark Drama

Seeking a poster that really stands out as a 'Festival Piece'. See the following lists for references:

QRVN Festival Poster Awards: https://www.snapvault.example/photos/officialqrvn/with/48203917562/

Here is the FULL RESOLUTION short film to take screen grabs and reference photos from:
https://www.filecrate.example/s/kp7wq2rzt91mxe4/Hollow014.mov?oref=e

We are open to much of anything, but this project needs to stand out as unique. On top of that, we are trying to push the angle of strangers THE HOLLOW in the forest (hence the name) and have thought of the opening sequence of the young man walking through the woods on the epic wide shot of being used for the poster art.

Various items need to be included on the poster: (Please feel free to reword as appropriate)

1) A FILM BY GORDON FAIRWEATHER
2) A DENNIS HOLMGRAVE PRODUCTION

All other taglines are optional and subject to addition or removal.

Please message with all other questions and comments.
Updates

Hey everyone, I apologize for not providing a high enough resolution copy of the short. I was told that this was the highest resolution until I got back straight from my editor who said it's a preliminary. Unfortunately, I do not have the ENTIRE film at top resolution. I will, however, attach high resolution .tiffs from various points of the film for use. https://www.filecrate.example/sh/wte8pqz41nd75ub/BBXKTmcPoLRWqDYe27fhZwNtb?dl=0

Industry/Entity Type

Film Production

Font styles to use
Serif
Sans Serif

Requirements
Must have
• 1) A FILM BY GORDON FAIRWEATHER
• 2) A DENNIS HOLMGRAVE PRODUCTION
• "THE HOLLOW" - Name of Film
Nice to have
• Tagline, but not necessary.

```html
<!DOCTYPE html>
<html lang="en">
<head>
<meta charset="utf-8">
<title>THE HOLLOW – Short Film Poster</title>
<link rel="stylesheet" href="https://fonts.googleapis.com/css2?family=Anton&family=Montserrat:wght@500&display=swap">
<style>
  :root {
    --stripe-oxblood: #6b1b18;
    --stripe-crimson: #b21f2f;
    --stripe-slate: #6a6558;
    --stripe-sand: #c99a5f;
    --title-white: #fbfaf7;
    --ink-black: #0b0908;
    --credit-grey: #9c9a98;
  }
  html, body {
    margin: 0;
    padding: 0;
    overflow: hidden;
    background: var(--ink-black);
  }
  .poster {
    position: relative;
    width: 800px;
    height: 1200px;
    overflow: hidden;
    background: var(--ink-black);
  }
  .poster-art {
    position: absolute;
    inset: 0;
    display: block;
  }
  .stripe-oxblood { fill: var(--stripe-oxblood); }
  .stripe-crimson { fill: var(--stripe-crimson); }
  .stripe-slate { fill: var(--stripe-slate); }
  .stripe-sand { fill: var(--stripe-sand); }
  .ground { fill: var(--ink-black); }
  .film-title {
    font-family: "Anton", "Impact", sans-serif;
    fill: var(--title-white);
  }
  .film-title-article {
    font-size: 80px;
    letter-spacing: 12px;
  }
  .film-title-main {
    font-size: 300px;
  }
  .director-credit {
    position: absolute;
    top: 523px;
    left: 0;
    width: 800px;
    margin: 0;
    text-align: center;
    font-family: "Montserrat", "Helvetica Neue", Arial, sans-serif;
    font-weight: 500;
    font-size: 17px;
    line-height: 22px;
    letter-spacing: 4.2px;
    color: var(--ink-black);
  }
  .production-credit {
    position: absolute;
    top: 1128px;
    left: 0;
    width: 800px;
    margin: 0;
    text-align: center;
    font-family: "Montserrat", "Helvetica Neue", Arial, sans-serif;
    font-weight: 500;
    font-size: 27px;
    line-height: 36px;
    letter-spacing: 3px;
    color: var(--credit-grey);
  }
</style>
</head>
<body>
  <main class="poster">
    <svg class="poster-art" width="800" height="1200" viewBox="0 0 800 1200" xmlns="http://www.w3.org/2000/svg">
      <defs>
        <linearGradient id="forest-shade" x1="0" y1="0" x2="0" y2="1">
          <stop offset="0" stop-color="#000" stop-opacity="0"/>
          <stop offset="0.35" stop-color="#000" stop-opacity="0.22"/>
          <stop offset="1" stop-color="#000" stop-opacity="0.45"/>
        </linearGradient>
      </defs>

      <g class="colour-stripes">
        <rect class="stripe-oxblood" x="0" y="0" width="200" height="1200"/>
        <rect class="stripe-crimson" x="200" y="0" width="200" height="1200"/>
        <rect class="stripe-slate" x="400" y="0" width="200" height="1200"/>
        <rect class="stripe-sand" x="600" y="0" width="200" height="1200"/>
      </g>

      <rect class="forest-scene" x="0" y="590" width="800" height="440" fill="url(#forest-shade)"
            role="img" aria-label="Silhouetted pine forest with a lone hiker carrying a backpack walking at the right"/>

      <path class="ground" d="M0 975 C 140 962 260 966 400 970 C 540 974 660 984 800 1010 L800 1200 L0 1200 Z"/>

      <g class="film-title" aria-label="THE HOLLOW">
        <text class="film-title-article" x="406" y="221" text-anchor="middle">THE</text>
        <text class="film-title-main" x="52" y="492" textLength="712" lengthAdjust="spacingAndGlyphs">HOLLOW</text>
      </g>
    </svg>

    <p class="director-credit">A FILM BY GORDON FAIRWEATHER</p>
    <p class="production-credit">A DENNIS HOLMGRAVE PRODUCTION</p>
  </main>
</body>
</html>
```